Willowbend Pharmacy Business Cards

I need a business card design and or template. Needs to convey a softer feel along with health and wellness. Please see attached logo and color scheme.

Industry/Entity Type

Pharmacy

Colors

Designer to choose colors to be used in the design.

Requirements
Must have
• I've added a second NEW colored logo I think I am going to go with the blue green logo.
• Needs to have the colors and feel of the logo attached.
• Dorian Kessel
• Pharmacy Manager
• willowbendpharmacy.example

```html
<!DOCTYPE html>
<html lang="en">
<head>
<meta charset="utf-8">
<title>Willowbend Pharmacy Business Cards</title>
<link href="https://fonts.googleapis.com/css2?family=Fira+Sans:wght@400;500;600&display=swap" rel="stylesheet">
<style>
  :root {
    --backdrop: #ece8e3;
    --paper: #ffffff;
    --pink: #e96b95;
    --green: #a3bf2b;
    --green-deep: #7a9726;
    --ink: #4d4d4f;
    --ink-soft: #5a5a5c;
  }
  * { box-sizing: border-box; margin: 0; padding: 0; }
  html, body { width: 1200px; height: 1200px; overflow: hidden; }
  body {
    background: var(--backdrop);
    font-family: "Fira Sans", sans-serif;
    position: relative;
  }
  .card {
    position: absolute;
    left: 210px;
    width: 798px;
    height: 442px;
    border-radius: 32px;
    overflow: hidden;
    box-shadow: 0 6px 18px rgba(0,0,0,0.18);
  }
  .card--front { top: 124px; background: var(--paper); }
  .card--back {
    top: 650px;
    background: linear-gradient(180deg, var(--green) 0%, #98b52a 50%, var(--green-deep) 100%);
    display: flex; align-items: center; justify-content: center;
  }
  .person { position: absolute; left: 72px; top: 72px; }
  .person__name { color: var(--pink); font-weight: 600; font-size: 28px; line-height: 1.2; }
  .person__role { color: var(--ink-soft); font-size: 18.5px; margin-top: 4px; }
  .rule {
    position: absolute; left: 73px; top: 178px;
    width: 48px; height: 2px; background: var(--green);
  }
  .contact {
    position: absolute; left: 72px; top: 220px;
    color: var(--ink-soft); font-size: 18px; line-height: 28px;
  }
  .contact__lines { list-style: none; margin-top: 12px; }
  .contact__lines li { display: flex; align-items: center; gap: 12px; }
  .contact__lines svg { width: 17px; height: 17px; margin-left: -2px; }
  .brand {
    position: absolute; right: 65px; top: 84px;
    display: flex; align-items: center; gap: 12px;
  }
  .brand__dot { width: 22px; height: 22px; border-radius: 50%; background: var(--green); }
  .brand__name { color: var(--ink); font-weight: 500; font-size: 28px; }
  .footer-band {
    position: absolute; left: 0; right: 0; bottom: 0; height: 72px;
    background: linear-gradient(180deg, var(--pink) 0%, var(--pink) 18%, var(--green) 42%, var(--green) 100%);
  }
  .site {
    position: absolute; right: 65px; bottom: 16px;
    color: #fff; font-weight: 500; font-size: 19px; letter-spacing: 0.5px;
    line-height: 24px;
  }
  .brand--reverse { position: static; gap: 20px; }
  .brand--reverse .brand__dot { width: 40px; height: 40px; background: #fff; }
  .brand--reverse .brand__name { color: #fff; font-size: 54px; font-weight: 600; }
</style>
</head>
<body>
  <section class="card card--front">
    <div class="footer-band" role="img" aria-label="Decorative pink and green wave band"></div>

    <div class="person">
      <h1 class="person__name">Dorian Kessel</h1>
      <p class="person__role">Pharmacy Manager</p>
    </div>
    <div class="rule"></div>

    <div class="contact">
      <p>999 Meadow Lane, Suite 999<br>Fairhaven, CA 99999</p>
      <ul class="contact__lines">
        <li>
          <svg viewBox="0 0 24 24" aria-hidden="true"><path d="M6.6 10.8a15 15 0 0 0 6.6 6.6l2.2-2.2c.3-.3.7-.4 1-.2 1.1.4 2.3.6 3.6.6.6 0 1 .4 1 1V20c0 .6-.4 1-1 1A17 17 0 0 1 3 4c0-.6.4-1 1-1h3.5c.6 0 1 .4 1 1 0 1.3.2 2.5.6 3.6.1.3 0 .7-.2 1z" fill="var(--pink)"/></svg>
          000-000-0000
        </li>
        <li>
          <svg viewBox="0 0 24 24" aria-hidden="true"><rect x="2.5" y="5" width="19" height="14" fill="none" stroke="var(--pink)" stroke-width="1.6"/><path d="M2.5 5l9.5 8 9.5-8M2.5 19l7-6.5M21.5 19l-7-6.5" fill="none" stroke="var(--pink)" stroke-width="1.6"/></svg>
          dorian@willowbendpharmacy.example
        </li>
      </ul>
    </div>

    <div class="brand">
      <span class="brand__dot"></span>
      <span class="brand__name">Willowbend Pharmacy</span>
    </div>

    <p class="site">willowbendpharmacy.example</p>
  </section>

  <section class="card card--back">
    <div class="brand brand--reverse">
      <span class="brand__dot"></span>
      <span class="brand__name">Willowbend Pharmacy</span>
    </div>
  </section>
</body>
</html>
```